Design einer Auto-Folie für KM-Bus
Zielgruppe
Privat - Autofolie für KM Bus 6.1 Camper Heckklappe entwerfen - eher handwerklich statt kreativ
Aufgabenstellung
* Maße 139 cm x 9,5 cm - Bitte unten genannte Flaggen einbauen
* Muster unten mit falschen Flaggen - müssen richtig ausgewählt und in Grösse angepasst werden.: See Draft_Design01.pdf
* Reihenfolge von links
* EU - DE - A - IT - CH - NL - ES - F - POR - visiting friends - LUMORA - UK - IRL - BEL - DAN - NOR - S - FIN -POL - CZ - GRI - BAYERN
* Lumora Rad - auswählen, welches am besten farblich passt
* Flaggen selber besorgen
* Maße Folie für Autotür (Heckklappe KM Bus Tolpe 6.1): 139 cm x 9,5 cm
* Einbauort siehe Foto KM Tolpe Weis Heckklappe unten - unter Falz
=> Endprodukt: Druckvorlage für Foliendruck erstellen

```html
<!DOCTYPE html>
<html lang="de">
<head>
<meta charset="utf-8">
<title>KM-Bus Heckklappen-Folie</title>
<link rel="stylesheet" href="https://fonts.googleapis.com/css2?family=Oswald:wght@600&display=swap">
<style>
  :root {
    --page: #f3f3f3;
    --strip-bg: #1c1c22;
    --eu-blue: #2b2f8f;
    --eu-gold: #ffdd00;
    --black: #111111;
    --red: #d2232a;
    --gold: #f5c400;
    --white: #ffffff;
    --uk-blue: #1f2f6b;
    --green: #1f9a4a;
    --nl-blue: #233f8c;
    --es-red: #c8102e;
    --es-yellow: #f7c600;
    --fr-blue: #1f3f99;
    --pt-green: #0a6a2e;
    --ie-orange: #f08a2c;
    --no-red: #ba0c2f;
    --no-blue: #00205b;
    --se-blue: #1e5aa8;
    --se-yellow: #f7cc16;
    --fi-blue: #1a4aa0;
    --pl-red: #d01f3b;
    --cz-blue: #17468f;
    --gr-blue: #1466b3;
    --vf-yellow: #f6d31a;
  }
  html, body {
    margin: 0;
    width: 1200px;
    height: 521px;
    overflow: hidden;
    background: var(--page);
  }
  .foil-strip {
    position: absolute;
    left: 10px;
    top: 219px;
    width: 1180px;
    height: 82px;
    display: block;
  }
  .strip-base { fill: var(--strip-bg); }
  .reflection { opacity: 0.42; }
  .headline {
    font-family: "Oswald", sans-serif;
    font-weight: 600;
    fill: var(--vf-yellow);
    stroke: #3a2a00;
    stroke-width: 1.2px;
    paint-order: stroke;
  }
  .club-name {
    font-family: "Oswald", sans-serif;
    font-weight: 600;
    fill: var(--vf-yellow);
  }
</style>
</head>
<body>
<svg class="foil-strip" viewBox="0 0 1790 125" xmlns="http://www.w3.org/2000/svg">
  <defs>
    <polygon id="eu-star" points="0,-5 1.18,-1.62 4.76,-1.55 1.9,0.62 2.94,4.05 0,2 -2.94,4.05 -1.9,0.62 -4.76,-1.55 -1.18,-1.62" fill="var(--eu-gold)"/>
    <clipPath id="uk-clip"><rect x="911" y="2" width="97" height="92"/></clipPath>
    <clipPath id="reflection-clip"><rect x="0" y="96" width="1790" height="27"/></clipPath>
    <linearGradient id="vf-fill" x1="0" y1="0" x2="1" y2="1">
      <stop offset="0" stop-color="#3d8fd6"/>
      <stop offset="0.5" stop-color="#dfeef9"/>
      <stop offset="1" stop-color="#3d8fd6"/>
    </linearGradient>
    <linearGradient id="bav-fill" x1="0" y1="0" x2="1" y2="1">
      <stop offset="0" stop-color="#3a8fd8"/>
      <stop offset="0.5" stop-color="#eef5fb"/>
      <stop offset="1" stop-color="#3a8fd8"/>
    </linearGradient>

    <g id="flag-row">
      <g class="flag flag-eu">
        <rect x="2" y="2" width="130" height="92" fill="var(--eu-blue)"/>
        <g transform="translate(67,48)">
          <use href="#eu-star" x="0" y="-28"/><use href="#eu-star" x="14" y="-24.2"/>
          <use href="#eu-star" x="24.2" y="-14"/><use href="#eu-star" x="28" y="0"/>
          <use href="#eu-star" x="24.2" y="14"/><use href="#eu-star" x="14" y="24.2"/>
          <use href="#eu-star" x="0" y="28"/><use href="#eu-star" x="-14" y="24.2"/>
          <use href="#eu-star" x="-24.2" y="14"/><use href="#eu-star" x="-28" y="0"/>
          <use href="#eu-star" x="-24.2" y="-14"/><use href="#eu-star" x="-14" y="-24.2"/>
        </g>
      </g>
      <g class="flag flag-de">
        <rect x="137" y="2" width="112" height="31" fill="var(--black)"/>
        <rect x="137" y="33" width="112" height="31" fill="var(--red)"/>
        <rect x="137" y="64" width="112" height="30" fill="var(--gold)"/>
      </g>
      <g class="flag flag-at">
        <rect x="254" y="2" width="85" height="92" fill="var(--red)"/>
        <rect x="254" y="33" width="85" height="30" fill="var(--white)"/>
      </g>
      <g class="flag flag-it">
        <rect x="344" y="2" width="25" height="92" fill="var(--green)"/>
        <rect x="369" y="2" width="25" height="92" fill="var(--white)"/>
        <rect x="394" y="2" width="24" height="92" fill="var(--red)"/>
      </g>
      <g class="flag flag-ch">
        <rect x="423" y="2" width="68" height="92" fill="var(--red)"/>
        <rect x="451" y="24" width="12" height="44" fill="var(--white)"/>
        <rect x="435" y="40" width="44" height="12" fill="var(--white)"/>
      </g>
      <g class="flag flag-nl">
        <rect x="496" y="2" width="59" height="31" fill="var(--red)"/>
        <rect x="496" y="33" width="59" height="30" fill="var(--white)"/>
        <rect x="496" y="63" width="59" height="31" fill="var(--nl-blue)"/>
      </g>
      <g class="flag flag-es">
        <rect x="560" y="2" width="55" height="92" fill="var(--es-red)"/>
        <rect x="560" y="25" width="55" height="46" fill="var(--es-yellow)"/>
        <rect x="567" y="36" width="12" height="20" fill="var(--es-red)" opacity="0.6" role="img" aria-label="Wappen Spanien"/>
      </g>
      <g class="flag flag-fr">
        <rect x="620" y="2" width="16" height="92" fill="var(--fr-blue)"/>
        <rect x="636" y="2" width="17" height="92" fill="var(--white)"/>
        <rect x="653" y="2" width="16" height="92" fill="var(--red)"/>
      </g>
      <g class="flag flag-pt">
        <rect x="674" y="2" width="18" height="92" fill="var(--pt-green)"/>
        <rect x="692" y="2" width="26" height="92" fill="var(--red)"/>
        <circle cx="692" cy="40" r="9" fill="var(--gold)" role="img" aria-label="Wappen Portugal"/>
      </g>
      <g class="panel visiting-friends">
        <rect x="723" y="2" width="183" height="92" fill="url(#vf-fill)" role="img" aria-label="Bayerisches Rautenmuster als Hintergrund"/>
        <text class="headline" x="814.5" y="22" text-anchor="middle" font-size="22" textLength="176" lengthAdjust="spacingAndGlyphs">VISITING FRIENDS</text>
        <circle cx="782" cy="62" r="7" fill="var(--vf-yellow)"/>
        <text class="club-name" x="796" y="71" font-size="24">LUMORA</text>
      </g>
      <g class="flag flag-uk" clip-path="url(#uk-clip)">
        <rect x="911" y="2" width="97" height="92" fill="var(--uk-blue)"/>
        <path d="M911 2 L1008 94 M1008 2 L911 94" stroke="var(--white)" stroke-width="16"/>
        <path d="M911 2 L1008 94 M1008 2 L911 94" stroke="var(--red)" stroke-width="5"/>
        <path d="M959.5 2 V94 M911 48 H1008" stroke="var(--white)" stroke-width="24"/>
        <path d="M959.5 2 V94 M911 48 H1008" stroke="var(--red)" stroke-width="13"/>
      </g>
      <g class="flag flag-ie">
        <rect x="1013" y="2" width="15" height="92" fill="var(--green)"/>
        <rect x="1028" y="2" width="16" height="92" fill="var(--white)"/>
        <rect x="1044" y="2" width="15" height="92" fill="var(--ie-orange)"/>
      </g>
      <g class="flag flag-be">
        <rect x="1064" y="2" width="12" height="92" fill="var(--black)"/>
        <rect x="1076" y="2" width="12" height="92" fill="var(--es-yellow)"/>
        <rect x="1088" y="2" width="12" height="92" fill="var(--red)"/>
      </g>
      <g class="flag flag-dk">
        <rect x="1105" y="2" width="56" height="92" fill="var(--red)"/>
        <rect x="1122" y="2" width="9" height="92" fill="var(--white)"/>
        <rect x="1105" y="43" width="56" height="9" fill="var(--white)"/>
      </g>
      <g class="flag flag-no">
        <rect x="1166" y="2" width="60" height="92" fill="var(--no-red)"/>
        <rect x="1183" y="2" width="14" height="92" fill="var(--white)"/>
        <rect x="1166" y="41" width="60" height="14" fill="var(--white)"/>
        <rect x="1187" y="2" width="6" height="92" fill="var(--no-blue)"/>
        <rect x="1166" y="45" width="60" height="6" fill="var(--no-blue)"/>
      </g>
      <g class="flag flag-se">
        <rect x="1231" y="2" width="65" height="92" fill="var(--se-blue)"/>
        <rect x="1249" y="2" width="11" height="92" fill="var(--se-yellow)"/>
        <rect x="1231" y="42" width="65" height="11" fill="var(--se-yellow)"/>
      </g>
      <g class="flag flag-fi">
        <rect x="1301" y="2" width="70" height="92" fill="var(--white)"/>
        <rect x="1320" y="2" width="12" height="92" fill="var(--fi-blue)"/>
        <rect x="1301" y="42" width="70" height="12" fill="var(--fi-blue)"/>
      </g>
      <g class="flag flag-pl">
        <rect x="1376" y="2" width="81" height="46" fill="var(--white)"/>
        <rect x="1376" y="48" width="81" height="46" fill="var(--pl-red)"/>
      </g>
      <g class="flag flag-cz">
        <rect x="1462" y="2" width="90" height="46" fill="var(--white)"/>
        <rect x="1462" y="48" width="90" height="46" fill="var(--pl-red)"/>
        <polygon points="1462,2 1507,48 1462,94" fill="var(--cz-blue)"/>
      </g>
      <g class="flag flag-gr">
        <rect x="1557" y="2" width="104" height="92" fill="var(--white)"/>
        <rect x="1557" y="2" width="104" height="10" fill="var(--gr-blue)"/>
        <rect x="1557" y="22" width="104" height="10" fill="var(--gr-blue)"/>
        <rect x="1557" y="42" width="104" height="10" fill="var(--gr-blue)"/>
        <rect x="1557" y="62" width="104" height="10" fill="var(--gr-blue)"/>
        <rect x="1557" y="82" width="104" height="12" fill="var(--gr-blue)"/>
        <rect x="1557" y="2" width="42" height="50" fill="var(--gr-blue)"/>
        <rect x="1573" y="2" width="10" height="50" fill="var(--white)"/>
        <rect x="1557" y="22" width="42" height="10" fill="var(--white)"/>
      </g>
      <g class="flag flag-by">
        <rect x="1666" y="2" width="120" height="92" fill="url(#bav-fill)" role="img" aria-label="Bayerische Rautenflagge mit Staatswappen"/>
      </g>
    </g>
  </defs>

  <rect class="strip-base" x="0" y="0" width="1790" height="125"/>
  <use href="#flag-row"/>
  <g class="reflection" clip-path="url(#reflection-clip)">
    <use href="#flag-row" transform="translate(0,190) scale(1,-1)"/>
  </g>
</svg>
</body>
</html>
```